The most modern business card ever !!!

Our company call “Vantilo”. Vantilo is a technology company specialized in cruises solutions. Out main product is a platform to reserve cruises. This is a revolutionary platform that make easier to travel agencies and final users to reserve cruises across dozen companies like tarvik, welbi, dpv, hbt, etc..We are a “start up”, with a young team of developers and we want to transmit it.. For it, we want something different, a modern business card that represent cruises and technology.. When someone receive this card, this person should say: wowww this is different… this is modern… this is a cruise related company..
Contact Information for Business Card
Requirements
Must have
- diferent, modern
Should not have
- traditions business card

```html
<!DOCTYPE html>
<html lang="en">
<head>
<meta charset="utf-8">
<title>Vantilo – Business Card</title>
<link rel="stylesheet" href="https://fonts.googleapis.com/css2?family=Exo+2:wght@500;600&family=Montserrat:wght@400;500&display=swap">
<style>
  :root {
    --backdrop-top: #bdbcba;
    --backdrop-bottom: #ffffff;
    --card-black: #000000;
    --brand-blue: #22a8e0;
    --ink-white: #ffffff;
    --photo-light: #5e5a59;
    --photo-dark: #262424;
  }
  html, body {
    margin: 0;
    width: 1200px;
    height: 1200px;
    overflow: hidden;
  }
  body {
    background: linear-gradient(180deg, var(--backdrop-top) 0%, #cfcecd 45%, var(--backdrop-bottom) 100%);
    position: relative;
  }
  .card {
    position: absolute;
    top: 334px;
    width: 295px;
    height: 506px;
    background: var(--card-black);
  }
  .card--front { left: 327px; }
  .card--back { left: 629px; }
  .card svg { display: block; width: 100%; height: 100%; }
  .brand-name {
    font-family: "Exo 2", sans-serif;
    font-weight: 600;
    fill: var(--ink-white);
    letter-spacing: 1px;
  }
  .person-name {
    font-family: "Exo 2", sans-serif;
    font-weight: 500;
    fill: var(--brand-blue);
    letter-spacing: 1.5px;
  }
  .person-title {
    font-family: "Exo 2", sans-serif;
    font-weight: 600;
    fill: var(--ink-white);
  }
  .contact-line {
    font-family: "Montserrat", sans-serif;
    font-weight: 400;
    fill: var(--ink-white);
    font-size: 14px;
  }
  .chevron-band { fill: var(--brand-blue); }
  .chevron-line { fill: none; stroke: var(--ink-white); stroke-width: 2; }
  .icon-disc { fill: var(--brand-blue); }
</style>
</head>
<body>

<div class="card card--front">
  <svg viewBox="0 0 369 633" xmlns="http://www.w3.org/2000/svg">
    <defs>
      <linearGradient id="photoFill" x1="0" y1="0" x2="0" y2="1">
        <stop offset="0" stop-color="var(--photo-light)"/>
        <stop offset="0.75" stop-color="var(--photo-dark)"/>
        <stop offset="1" stop-color="#000"/>
      </linearGradient>
    </defs>
    <rect class="cruise-photo" x="0" y="0" width="369" height="215" fill="url(#photoFill)" role="img" aria-label="Black and white aerial photo of a cruise ship deck at sea"/>

    <text class="brand-name" x="184" y="80" font-size="58" text-anchor="middle">Vantilo</text>

    <path class="chevron-band" d="M0,298 L165,118 Q186,98 207,118 L369,290 L369,389 L187,200 L0,395 Z"/>
    <path class="chevron-line" d="M0,330 L170,150 Q187,134 204,150 L369,323"/>
    <path class="chevron-line" d="M0,430 L187,233 L369,423"/>

    <text class="person-name" x="184" y="362" font-size="26" text-anchor="middle">Your Name</text>
    <text class="person-title" x="184" y="384" font-size="18" text-anchor="middle">Title</text>

    <g class="contact-address">
      <circle class="icon-disc" cx="184" cy="432" r="14"/>
      <path d="M184,423 a5.5,5.5 0 0 1 5.5,5.5 c0,4 -5.5,10 -5.5,10 c0,0 -5.5,-6 -5.5,-10 a5.5,5.5 0 0 1 5.5,-5.5 z" fill="#fff"/>
      <circle cx="184" cy="428.5" r="2" fill="var(--brand-blue)"/>
      <text class="contact-line" x="184" y="462" text-anchor="middle">Your Address Will Be Here</text>
      <text class="contact-line" x="184" y="481" text-anchor="middle">123, xyz 1122</text>
    </g>

    <g class="contact-phone">
      <circle class="icon-disc" cx="184" cy="508" r="14"/>
      <path d="M178,500 l3,-1 l2.5,5 l-2,1.5 q1.5,3.5 5,5 l1.5,-2 l5,2.5 l-1,3 q-1,1.5 -3,1.5 q-7,-1 -11,-8 q-1.5,-3 0,-7.5 z" fill="#fff"/>
      <text class="contact-line" x="184" y="539" text-anchor="middle">000 0000 12345</text>
    </g>

    <g class="contact-email">
      <circle class="icon-disc" cx="184" cy="564" r="14"/>
      <rect x="176" y="558.5" width="16" height="11" fill="none" stroke="#fff" stroke-width="1.6"/>
      <path d="M176,558.5 L184,565 L192,558.5 M176,569.5 L181.5,564 M192,569.5 L186.5,564" fill="none" stroke="#fff" stroke-width="1.4"/>
      <text class="contact-line" x="184" y="596" text-anchor="middle">info@youremail.com</text>
    </g>
  </svg>
</div>

<div class="card card--back">
  <svg viewBox="0 0 369 633" xmlns="http://www.w3.org/2000/svg">
    <path class="chevron-band" d="M0,298 L165,118 Q186,98 207,118 L369,290 L369,389 L187,200 L0,395 Z"/>
    <path class="chevron-line" d="M0,330 L170,150 Q187,134 204,150 L369,323"/>
    <path class="chevron-line" d="M0,430 L187,233 L369,423"/>
    <text class="brand-name" x="184" y="476" font-size="58" text-anchor="middle">Vantilo</text>
  </svg>
</div>

</body>
</html>
```